VeLT Record Shredding professional postcard

I'm looking for a postcard design that tells a story in very few words about how important it is to protect yourself your family and your clients against sensitive information and identity theft. My website is veltrecordshredding.net if you are looking for text to put on card. Would like "secure and certified destruction of your data and media" on the postcard.

Target Market(s)

Commercial and residential.

Industry/Entity Type

Business Service

Font styles to use
Serif

Colors
000000

Requirements
Must have
• A pic, 1-855-318-4096 phone number, veltrecordshredding.net web address area for postage must be double sided. Definitely want it eye catching. Must have an area for postage and mailing address. Would like to see glossy on one side and the other side not glossy

```html
<!DOCTYPE html>
<html lang="en">
<head>
<meta charset="utf-8">
<title>VeLT Record Shredding – Postcard</title>
<link href="https://fonts.googleapis.com/css2?family=Oswald:wght@300;500;700&family=Poppins:wght@500&family=Open+Sans:wght@400;700&display=swap" rel="stylesheet">
<style>
  :root{
    --ink:#000000;
    --card-black:#0b0d0f;
    --bar:#2a2c2e;
    --white:#ffffff;
    --blue:#3f8fe6;
    --blue-line:#1f63c9;
    --green:#7cc242;
    --teal:#16786b;
    --muted:#cfd3d6;
    --stage-top:#b9b9b9;
    --stage-bottom:#6d6d6d;
  }
  *{box-sizing:border-box;margin:0;padding:0}
  html,body{width:1200px;height:1200px;overflow:hidden}
  body{background:linear-gradient(var(--stage-top),var(--stage-bottom));position:relative;font-family:"Open Sans",sans-serif}
  .postcard{position:absolute;left:190px;width:820px;height:525px;background:var(--card-black);overflow:hidden;box-shadow:0 6px 18px rgba(0,0,0,.45)}
  .postcard--front{top:45px}
  .postcard--back{top:625px}
  .postcard svg.art{position:absolute;inset:0}
  .abs{position:absolute;white-space:nowrap}
  .brand{width:240px;display:flex;flex-direction:column;align-items:center;gap:8px;color:var(--white);font-family:"Poppins",sans-serif;font-weight:500;font-size:19px;line-height:1}
  .brand__dot{width:46px;height:46px;border:2px solid var(--white);border-radius:50%}
  .cond{font-family:"Oswald",sans-serif;line-height:1}
  .headline__kicker{color:var(--blue);font-weight:300;font-size:30px}
  .headline__main{color:var(--white);font-weight:700;font-size:48px;transform:scaleY(1.08);transform-origin:left bottom}
  .headline__of{color:var(--green);font-weight:300;font-size:37px}
  .headline__data{color:var(--white);font-weight:700;font-size:60px}
  .headline__data span{font-weight:300}
  .headline__media{color:var(--green);font-weight:700;font-size:76px}
  .contact{display:flex;align-items:center;gap:8px;color:var(--white)}
  .contact--phone{font-family:"Oswald",sans-serif;font-weight:500;font-size:31px}
  .contact--web{font-family:"Oswald",sans-serif;font-weight:300;font-size:16px}
  .about__title{color:var(--white);font-family:"Oswald",sans-serif;font-weight:500;font-size:14px}
  .about__text{position:absolute;left:35px;top:140px;width:355px;color:var(--muted);font-size:11.4px;line-height:14.2px;text-align:justify;white-space:normal}
</style>
</head>
<body>

<!-- FRONT -->
<section class="postcard postcard--front">
  <svg class="art" width="820" height="525" viewBox="0 0 820 525">
    <defs>
      <radialGradient id="photoTone" cx="70%" cy="45%" r="70%">
        <stop offset="0" stop-color="#8fa7b8"/>
        <stop offset=".45" stop-color="#4f6070"/>
        <stop offset="1" stop-color="#16222c"/>
      </radialGradient>
    </defs>
    <path role="img" aria-label="Photo: businessman in a suit holding his hands around a glowing padlock shield over a digital code backdrop"
          d="M484 0 C385 120 348 330 462 462 L820 462 L820 0 Z" fill="url(#photoTone)"/>
    <path d="M478 0 C378 120 342 330 452 462" fill="none" stroke="var(--white)" stroke-width="6"/>
    <rect x="0" y="462" width="820" height="63" fill="var(--bar)"/>
    <rect x="0" y="460" width="820" height="3" fill="var(--blue-line)"/>
    <circle cx="658" cy="452" r="64" fill="var(--white)"/>
    <circle cx="658" cy="452" r="58" fill="var(--teal)"/>
    <circle cx="658" cy="452" r="44" fill="none" stroke="var(--white)" stroke-width="2"/>
    <g transform="translate(76 497)" fill="none" stroke="var(--green)" stroke-width="2">
      <circle r="8"/>
      <path d="M-3 -4 q-1 5 4 8 l2 -2 -2 -2 -1 1 q-2 -1 -2 -3 l1 -1 -2 -2 z" fill="var(--green)" stroke="none"/>
    </g>
    <g transform="translate(388 492)" fill="none" stroke="var(--green)" stroke-width="1.4">
      <circle r="7"/><ellipse rx="3" ry="7"/><path d="M-7 0 H7 M-6 -3.5 H6 M-6 3.5 H6"/>
    </g>
  </svg>

  <div class="abs brand" style="left:40px;top:38px"><span class="brand__dot"></span>VeLT Record Shredding</div>
  <div class="abs cond headline__kicker" style="left:53px;top:154px">SECURE AND CERTIFIED</div>
  <div class="abs cond headline__main" style="left:53px;top:192px">DESTRUCTION</div>
  <div class="abs cond headline__of" style="left:53px;top:253px">OF YOUR</div>
  <div class="abs cond headline__data" style="left:53px;top:288px">DATA <span>&amp;</span></div>
  <div class="abs cond headline__media" style="left:53px;top:344px">MEDIA</div>
  <div class="abs contact contact--phone" style="left:98px;top:472px">1-855-318-4096</div>
  <div class="abs contact contact--web" style="left:402px;top:480px">veltrecordshredding.net</div>
</section>

<!-- BACK -->
<section class="postcard postcard--back" style="background:var(--white)">
  <svg class="art" width="820" height="525" viewBox="0 0 820 525">
    <path d="M0 0 L274 0 C420 80 500 330 390 525 L0 525 Z" fill="var(--card-black)"/>
    <path d="M274 0 C420 80 500 330 390 525" fill="none" stroke="var(--green)" stroke-width="4"/>
    <rect x="713" y="27" width="76" height="76" fill="none" stroke="#333" stroke-width="1.5"/>
    <g stroke="#555" stroke-width="1.2">
      <line x1="544" y1="230" x2="806" y2="230"/>
      <line x1="544" y1="281" x2="806" y2="281"/>
      <line x1="544" y1="332" x2="806" y2="332"/>
    </g>
    <circle cx="116" cy="388" r="52" fill="var(--white)"/>
    <circle role="img" aria-label="Photo: shredding truck parked outside" cx="116" cy="388" r="48" fill="#a0684f"/>
    <circle cx="267" cy="388" r="52" fill="var(--white)"/>
    <circle role="img" aria-label="Photo: secure shredding bin in a dark room" cx="267" cy="388" r="48" fill="#4a4542"/>
    <g transform="translate(43 474)" fill="none" stroke="var(--green)" stroke-width="2">
      <circle r="8"/>
      <path d="M-3 -4 q-1 5 4 8 l2 -2 -2 -2 -1 1 q-2 -1 -2 -3 l1 -1 -2 -2 z" fill="var(--green)" stroke="none"/>
    </g>
    <g transform="translate(43 506)" fill="none" stroke="var(--green)" stroke-width="1.4">
      <circle r="7"/><ellipse rx="3" ry="7"/><path d="M-7 0 H7 M-6 -3.5 H6 M-6 3.5 H6"/>
    </g>
  </svg>

  <div class="abs brand" style="left:40px;top:18px"><span class="brand__dot"></span>VeLT Record Shredding</div>
  <div class="abs about__title" style="left:35px;top:110px">ABOUT US</div>
  <p class="about__text">VeLT Record Shredding was founded in 2017 by Daniel Harwood, a long time business owner who was born and raised on Long Island. Daniel has worked in the data and equipment destruction area for many years. As a result, he saw the need for certified on site destruction of data media, which is not only convenient for clients but also highly secure. We provide a unique data destruction service by not only picking up your data media, but actually securely destroying the data and media on your site. This provides assurance to our clients that the data in readable form never leaves their site. We are primarily providing service to Nassau and Suffolk counties on Long Island NY, but are available to the tri-state area. You can contact us using the form on the Request Information page or call us at 1-855-318-4096</p>
  <div class="abs contact contact--phone" style="left:58px;top:448px">1-855-318-4096</div>
  <div class="abs contact contact--web" style="left:58px;top:493px;font-size:20px">veltrecordshredding.net</div>
</section>

</body>
</html>
```